依頼詳細
デザイン住宅の看板デザインをお願いします。
生活道路沿いの路上看板のデザインになります。
事務所上の看板デザインに沿って頂き、シンプルで目立つ看板のデザインでお願いします。
記載項目
会社名:株式会社キリノハコビヤ
電話番号:0574-83-5167
ロゴ(添付ファイル)
看板写真(添付ファイル:宮鶴屋さんの下部分になります)
参考:事務所上の看板(添付ファイル)
希望イメージ
希望する色
水色系、無彩色系
納品ファイル
• 高解像度JPG (.jpg)
• イラストレーター形式 (.ai)
• フォトショップ形式 (.psd)
• PNG形式 (.png)
補足説明
〇想い
高性能でカッコいい家をどこよりもお値打ちに
家づくりは楽しくなくてはならない
家族みんなが毎日笑顔になるオリジナルの家
想いをカタチにできる家
地震に強く、高性能は当たり前

〇メインターゲット
子育て世代・共働き世代
大手ハウスメーカー層から降りてこられるお客様
デザイン住宅(設計事務所)から降りてこられるお客様
看板サイズ 幅1350mm×高さ2500mm

看板の位置の写真の追加させて頂きます。
■ 選んだ理由

シンプルさの中に、親しみを一番感じました。
優しいコントラストの中に、温かみも含まれてると感じ、
こちらのご提案を採用させて頂きました。

■ 提案者全員のお礼・コメント

たくさんのご提案を頂き、ありがとうございました!
正直こんなにご提案頂けるとは思っておらず、
皆さまのデザインに対する想いがすごく伝わり、とても勉強になりました。
次の機会があれば、またご依頼させて頂きたいと思います。
ありがとうございました!

```html
<!DOCTYPE html>
<html lang="ja">
<head>
<meta charset="UTF-8">
<title>キリノハコビヤ 路上看板</title>
<link rel="stylesheet" href="https://fonts.googleapis.com/css2?family=Cormorant+Garamond:wght@300;400&family=Noto+Sans+JP:wght@300;500&display=swap">
<style>
  :root {
    --page: #ffffff;
    --mauve: #b38ea2;
    --mauve-text: #f6ecf0;
    --brown: #4b2a2f;
    --brown-text: #efe3e5;
    --white: #ffffff;
  }
  * { margin: 0; padding: 0; box-sizing: border-box; }
  html, body {
    width: 813px; height: 1200px; overflow: hidden;
    background: var(--page);
  }
  .sign {
    position: absolute;
    left: 144px; top: 95px;
    width: 534px; height: 989px;
    display: flex; flex-direction: column;
  }
  .sign__top {
    height: 387px;
    background: var(--mauve);
    display: flex; flex-direction: column; align-items: center;
  }
  .brand-mark {
    margin-top: 150px;
    display: flex; align-items: center; gap: 10px;
    font-family: "Cormorant Garamond", serif;
    font-weight: 300;
    font-size: 24px;
    letter-spacing: 0.18em;
    color: var(--mauve-text);
  }
  .brand-mark__dot {
    width: 12px; height: 12px; border-radius: 50%;
    border: 1.5px solid var(--mauve-text);
  }
  .tagline {
    margin-top: 78px;
    font-family: "Noto Sans JP", sans-serif;
    font-weight: 300;
    font-size: 19px;
    letter-spacing: 0.28em;
    color: var(--mauve-text);
  }
  .sign__photos {
    height: 244px;
    display: flex; gap: 4px;
    background: var(--page);
  }
  .photo { flex: 1; }
  .photo--modern {
    background: linear-gradient(180deg, #8fb4d8 0%, #b6cde0 30%, #3a3a3c 45%, #2a2a2c 75%, #8a8a86 100%);
  }
  .photo--cottage {
    background: linear-gradient(180deg, #cfe0ee 0%, #e4e8ea 30%, #c98f6e 42%, #efe8dc 60%, #c7b79a 100%);
  }
  .sign__bottom {
    flex: 1;
    background: var(--brown);
    display: flex; flex-direction: column; align-items: center;
    color: var(--brown-text);
    position: relative;
  }
  .wordmark {
    margin-top: 112px;
    font-family: "Cormorant Garamond", serif;
    font-weight: 300;
    font-size: 35px;
    letter-spacing: 0.08em;
  }
  .wordmark-rule {
    position: absolute;
    left: 478px; top: 104px;
    width: 1px; height: 58px;
    background: var(--brown-text);
  }
  .studio {
    margin-top: 6px;
    font-family: "Cormorant Garamond", serif;
    font-weight: 400;
    font-size: 14px;
    letter-spacing: 0.42em;
  }
  .company {
    margin-top: 34px;
    font-family: "Noto Sans JP", sans-serif;
    font-weight: 500;
    font-size: 16px;
    color: var(--white);
  }
  .phone {
    margin-top: 2px;
    font-family: "Noto Sans JP", sans-serif;
    font-weight: 300;
    font-size: 42px;
    letter-spacing: 0.01em;
    line-height: 1.1;
    color: var(--white);
  }
</style>
</head>
<body>
  <div class="sign">
    <section class="sign__top">
      <div class="brand-mark"><span class="brand-mark__dot"></span>KIRINO HAKOBIYA</div>
      <p class="tagline">想いをカタチにできる家</p>
    </section>
    <section class="sign__photos">
      <div class="photo photo--modern" role="img" aria-label="黒い外壁と木目アクセントのモダンな住宅の外観写真"></div>
      <div class="photo photo--cottage" role="img" aria-label="オレンジ瓦屋根と白壁の平屋住宅と庭の外観写真"></div>
    </section>
    <section class="sign__bottom">
      <p class="wordmark">KIRINO HAKOBIYA</p>
      <span class="wordmark-rule"></span>
      <p class="studio">MINO STUDIO</p>
      <p class="company">株式会社キリノハコビヤ</p>
      <p class="phone">0574-83-5167</p>
    </section>
  </div>
</body>
</html>
```